verdant harbour requires some business cards

I need some business cards created that feature the company's newly designed logo. The business cards need to be be double sided and be a standard Australian size of 90mm x 55mm

Target Market(s)

business professionals, company executives, local goverment

Industry/Entity Type

Business

Requirements
Must have
• Company's logo
• The information section must include
• Individual name:
• Position:
• Phone:
• Address:
• Email:
• Website: www.verdantharbour.example
• The cards need to be easily formatted so I can enter staff members details positions etc...
• I plan to get these printed at deskmarket so can you please ensure that all designs meet their printing requirements http://www.deskmarket.example/retail/b2c/opsProductCreate.do?qty=1&cardQty=1000&sided=double&productname=colourbusinesscards&category=businesscards
Nice to have
• I might like to see some of the services we offer printed on one of the faces:
• Lighting Design (architectural, commercial, residential, theatrical ,exterior, interior) Lighting Consultancy, Theatrical Consultancy

```html
<!DOCTYPE html>
<html lang="en">
<head>
<meta charset="utf-8">
<title>verdant harbour business cards</title>
<link href="https://fonts.googleapis.com/css2?family=Mulish:ital,wght@0,300;0,400;0,700;1,400&display=swap" rel="stylesheet">
<style>
  :root {
    --backdrop: #e6e7e9;
    --card: #ffffff;
    --ink: #3a3a3c;
    --ink-soft: #4a4a4c;
    --accent: #1b9dd9;
    --shadow: rgba(0,0,0,0.28);
  }
  * { margin: 0; padding: 0; box-sizing: border-box; }
  html, body {
    width: 1200px; height: 1000px; overflow: hidden;
    background: var(--backdrop);
    font-family: "Mulish", sans-serif;
    color: var(--ink);
  }
  .canvas { position: relative; width: 1200px; height: 1000px; }
  .card {
    position: absolute;
    width: 349px; height: 213px;
    background: var(--card);
    box-shadow: 2px 2px 3px var(--shadow);
    overflow: hidden;
  }
  .card--front { left: 202px; top: 362px; }
  .card--back { left: 650px; top: 359px; }

  .brand { position: absolute; display: flex; align-items: center; gap: 10px; }
  .brand__dot { border-radius: 50%; background: var(--accent); flex: none; }
  .brand__name { font-weight: 300; color: var(--ink); white-space: nowrap; letter-spacing: -0.5px; }

  .card--front .brand { left: 40px; top: 74px; }
  .card--front .brand__dot { width: 22px; height: 22px; }
  .card--front .brand__name { font-size: 33px; }
  .tagline {
    position: absolute; left: 76px; top: 129px;
    font-size: 12.5px; font-style: italic; color: var(--ink-soft);
  }

  .card--back .brand { left: 22px; top: 44px; }
  .card--back .brand__dot { width: 50px; height: 50px; }

  .contact { position: absolute; left: 108px; top: 19px; }
  .contact__name { font-size: 15px; font-weight: 700; color: var(--ink); margin-bottom: 2px; }
  .contact__row {
    display: flex; align-items: center; gap: 7px;
    font-size: 11px; color: var(--ink-soft); height: 19.5px;
  }
  .contact__row svg { width: 17px; height: 14px; flex: none; }
  .contact__address { font-size: 11px; line-height: 13px; color: var(--ink-soft); margin: 4px 0 0 24px; }

  .services { position: absolute; left: 14px; top: 151px; }
  .services__title { font-size: 12.5px; color: var(--ink-soft); line-height: 14px; }
  .services__list {
    margin-left: 24px; font-size: 9.2px; font-style: italic; color: var(--ink); white-space: nowrap;
  }
  .services__list .sep { color: var(--accent); font-style: normal; }
  .band { position: absolute; left: 37px; top: 182px; right: 0; bottom: 0; background: var(--accent); }
</style>
</head>
<body>
<div class="canvas">
  <section class="card card--front">
    <div class="brand">
      <span class="brand__dot"></span>
      <span class="brand__name">verdant harbour</span>
    </div>
    <p class="tagline">Lighting &amp; Theatrical Consultancy</p>
  </section>

  <section class="card card--back">
    <div class="brand"><span class="brand__dot" role="img" aria-label="verdant harbour"></span></div>
    <div class="contact">
      <p class="contact__name">Firstname Lastname</p>
      <p class="contact__row">
        <svg viewBox="0 0 17 14"><rect x="1" y="2" width="15" height="10" fill="none" stroke="#1b9dd9" stroke-width="1.3"/><path d="M1 2l7.5 6L16 2" fill="none" stroke="#1b9dd9" stroke-width="1.3"/></svg>
        example@email.com
      </p>
      <p class="contact__row">
        <svg viewBox="0 0 17 14"><path d="M4 1.5l2.3 2.4-1.3 1.7c.8 1.7 2 2.9 3.6 3.7l1.6-1.3 2.5 2.2-1.4 1.8C7 11.6 3.6 8.2 2.5 3z" fill="#1b9dd9"/></svg>
        +61 8 95550142
      </p>
      <p class="contact__row">
        <svg viewBox="0 0 17 14"><g fill="none" stroke="#1b9dd9" stroke-width="1.1"><circle cx="8.5" cy="7" r="6"/><ellipse cx="8.5" cy="7" rx="2.6" ry="6"/><path d="M2.5 7h12M3.5 4h10M3.5 10h10"/></g></svg>
        www.verdantharbour.example
      </p>
      <p class="contact__address">PO Box 482, Perth WA 6000<br>Australia</p>
    </div>
    <div class="services">
      <p class="services__title">Lighting Design</p>
      <p class="services__list">architectural <span class="sep">•</span> commercial <span class="sep">•</span> residential <span class="sep">•</span> theatrical <span class="sep">•</span> exterior <span class="sep">•</span> interior</p>
    </div>
    <div class="band"></div>
  </section>
</div>
</body>
</html>
```